" A estrutura da empresa será inicialmente simples e prática. Terá a unidade fabril, onde serão produzidos os biscoitos e uma central de entrega, para os pedidos feitos por telefone e pela internet. Os alimentos de consumo rápido ou de conveniência como os biscoitos apresentam-se como uma solução para os consumidores a praticidade da realização de um lanche rápido que caiba no dia a dia. Assim, o público alvo da Marpenelo’s é constituído principalmente por empresas que revendem os produtos (como supermercados, lojas de conveniência, padarias, clínicas, etc) e pelos clientes finais em menor quantidade representando aqui o consumidor final. "

```html
<!DOCTYPE html>
<html lang="pt-BR">
<head>
<meta charset="utf-8">
<title>Marpenelo’s — Rótulos de embalagem</title>
<link rel="stylesheet" href="https://fonts.googleapis.com/css2?family=Dancing+Script:wght@600&display=swap">
<style>
  :root{
    --bg:#f1eeea;
    --wine:#8a1f3a;
    --wine-dark:#6e1530;
    --cream:#fbf6f1;
    --stitch:#f3d9df;
    --lid:#ffffff;
    --lid-edge:#dcd8d4;
  }
  html,body{margin:0;padding:0;overflow:hidden;}
  body{
    width:1200px;height:1200px;background:var(--bg);
    font-family:"Dancing Script",cursive;
    position:relative;
  }
  .lid-label{
    position:absolute;left:300px;top:90px;width:600px;height:600px;
    border-radius:50%;background:var(--lid);
    box-shadow:0 0 0 10px var(--lid-edge) inset;
    display:flex;flex-direction:column;align-items:center;justify-content:center;
  }
  .brand-name{color:var(--wine);font-weight:600;margin:0;line-height:1;white-space:nowrap;}
  .lid-label .brand-name{font-size:104px;}
  .tagline{font-weight:600;margin:0;line-height:1;white-space:nowrap;}
  .lid-label .tagline{color:var(--wine);font-size:38px;margin-top:20px;}
  .wrap-band{position:absolute;left:0;top:790px;width:1200px;height:300px;}
  .wrap-band svg{position:absolute;inset:0;}
  .seal-text{
    position:absolute;left:480px;top:30px;width:240px;height:240px;
    display:flex;flex-direction:column;align-items:center;justify-content:center;
  }
  .seal-text .brand-name{color:var(--cream);font-size:44px;}
  .seal-text .tagline{color:var(--cream);font-size:17px;margin-top:10px;}
</style>
</head>
<body>
  <section class="lid-label">
    <h1 class="brand-name">Marpenelo’s</h1>
    <p class="tagline">Biscoitos Amanteigados</p>
  </section>

  <section class="wrap-band">
    <svg width="1200" height="300" viewBox="0 0 1200 300" aria-hidden="true">
      <rect class="band" x="0" y="95" width="1200" height="110" fill="var(--wine)"/>
      <line x1="0" y1="110" x2="1200" y2="110" stroke="var(--stitch)" stroke-width="3" stroke-dasharray="12 8"/>
      <line x1="0" y1="190" x2="1200" y2="190" stroke="var(--stitch)" stroke-width="3" stroke-dasharray="12 8"/>
      <circle cx="600" cy="150" r="150" fill="var(--wine-dark)"/>
      <circle cx="600" cy="150" r="135" fill="var(--wine)"/>
      <circle cx="600" cy="150" r="120" fill="none" stroke="var(--stitch)" stroke-width="3" stroke-dasharray="10 7"/>
    </svg>
    <div class="seal-text">
      <p class="brand-name">Marpenelo’s</p>
      <p class="tagline">Biscoitos Amanteigados</p>
    </div>
  </section>
</body>
</html>
```